Business Card Design

I have a very clear idea of what I want. I just do not know how to do the graphic design to match it.

On the front I want the uploaded image with the horse and the two people.
I want

Bottom left hand corner
Lenny Firth
0472 316 508

Bottom right
There is maroon block with Morris Tane Practitioner Group Logo
Next to that I want the Stable Arc tile about the same size ( attached psd file)

On the back I want a plain colour (white) with the information

Lenny Firth
Equine Performance
Brindle4Ponies and Acupuncture
Horsemanship Lessons and Clinics
Horse Training

lfirth@critterloop.com.au
FB/lenny.firth.263
StableArc.com.au

Lenny Firth
0472 316 508
lfirth@critterloop.com.au

```html
<!DOCTYPE html>
<html lang="en">
<head>
<meta charset="utf-8">
<title>Lenny Firth – Business Card</title>
<link href="https://fonts.googleapis.com/css2?family=Great+Vibes&family=Open+Sans:wght@400;600&family=Cinzel:wght@400&display=swap" rel="stylesheet">
<style>
  :root {
    --bg: #e9e7e4;
    --navy: #1f3a6e;
    --navy-dark: #17294f;
    --sand-light: #d9bf8c;
    --sand-mid: #c4a26a;
    --sand-dark: #9a7a4a;
    --brown: #3b2415;
    --tile-brown: #6b4327;
    --tile-cream: #f5efe2;
    --maroon: #6e2a1c;
    --white: #ffffff;
  }
  * { box-sizing: border-box; margin: 0; padding: 0; }
  html, body { width: 1200px; height: 873px; overflow: hidden; }
  body {
    background: var(--bg);
    font-family: "Open Sans", Arial, sans-serif;
    position: relative;
  }
  .card {
    position: absolute;
    top: 266px;
    width: 540px;
    height: 340px;
    box-shadow: 0 6px 18px rgba(0,0,0,.18);
    overflow: hidden;
  }
  /* FRONT */
  .card--front { left: 40px; border: 7px solid var(--navy); }
  .front__photo {
    position: absolute; inset: 0;
    background: radial-gradient(ellipse at 40% 45%, var(--sand-light), var(--sand-mid) 60%, var(--sand-dark));
  }
  .front__tagline {
    position: absolute; top: 26px; right: 34px; width: 300px;
    text-align: center; color: var(--brown);
  }
  .tagline__lead { font-family: "Cinzel", Georgia, serif; font-size: 17px; letter-spacing: 1px; }
  .tagline__your { font-family: "Great Vibes", cursive; font-size: 24px; display: block; margin: 2px 0 -14px 60px; text-align: left; }
  .tagline__main { font-family: "Great Vibes", cursive; font-size: 74px; line-height: 1; }
  .front__contact {
    position: absolute; left: 22px; bottom: 22px; color: var(--brown);
  }
  .front__name { font-size: 20px; font-weight: 400; }
  .front__phone { font-size: 11px; margin-top: 2px; }
  .front__badges {
    position: absolute; right: 16px; bottom: 16px;
    display: flex; align-items: flex-end; gap: 10px;
  }
  .app-tile {
    border-radius: 12px; background: var(--tile-cream);
    border: 4px solid var(--tile-brown);
    display: flex; align-items: center; justify-content: center;
    color: var(--navy); font-weight: 600; text-align: center;
  }
  .app-tile--small { width: 62px; height: 52px; font-size: 10px; }
  .partner-block {
    width: 86px; height: 64px; background: var(--maroon);
    color: var(--sand-light); font-size: 9px; line-height: 1.25;
    display: flex; align-items: center; justify-content: center;
    text-align: center; padding: 6px;
  }
  /* BACK */
  .card--back { left: 620px; background: var(--white); color: var(--navy); }
  .app-tile--large {
    position: absolute; top: 30px; left: 120px;
    width: 120px; height: 100px; font-size: 17px;
    border-width: 6px; border-radius: 18px;
    box-shadow: 0 4px 0 #8b5a37, 0 8px 14px rgba(0,0,0,.2);
  }
  .contact-list { position: absolute; list-style: none; font-size: 12px; }
  .contact-list li { display: flex; align-items: center; gap: 8px; margin-bottom: 9px; }
  .contact-list--direct { left: 34px; top: 170px; }
  .contact-list--online { left: 250px; top: 262px; }
  .icon { width: 20px; height: 20px; flex: none; }
  .profile { position: absolute; left: 300px; top: 120px; }
  .profile__name { font-size: 22px; font-weight: 400; margin-bottom: 4px; }
  .services { list-style: none; font-size: 11px; line-height: 1.45; }
  .services li { display: flex; align-items: center; gap: 5px; }
  .tick { width: 10px; height: 10px; flex: none; }
</style>
</head>
<body>

<section class="card card--front">
  <div class="front__photo" role="img" aria-label="Photograph of a rider and a trainer working a bay horse on a sandy arena, seen from above"></div>
  <div class="front__tagline">
    <div class="tagline__lead">HOW YOU EVER GONNA KNOW</div>
    <span class="tagline__your">Your</span>
    <div class="tagline__main">Potential</div>
  </div>
  <div class="front__contact">
    <div class="front__name">Lenny Firth</div>
    <div class="front__phone">0472 316 508</div>
  </div>
  <div class="front__badges">
    <div class="app-tile app-tile--small">Stable Arc</div>
    <div class="partner-block">Morris Tane Practitioner Group</div>
  </div>
</section>

<section class="card card--back">
  <div class="app-tile app-tile--large">Stable Arc</div>

  <ul class="contact-list contact-list--direct">
    <li>
      <svg class="icon" viewBox="0 0 20 20"><circle cx="10" cy="10" r="10" fill="var(--navy)"/><path d="M7 5l2 2-1.2 1.5a7 7 0 0 0 3.7 3.7L13 11l2 2-1.5 1.6C9.5 14.5 5.5 10.5 5.4 6.5z" fill="#fff"/></svg>
      <span>0472 316 508</span>
    </li>
    <li>
      <svg class="icon" viewBox="0 0 20 20"><circle cx="10" cy="10" r="10" fill="var(--navy)"/><rect x="5" y="6.5" width="10" height="7" fill="none" stroke="#fff" stroke-width="1.2"/><path d="M5 6.5l5 4 5-4" fill="none" stroke="#fff" stroke-width="1.2"/></svg>
      <span>lfirth@critterloop.com.au</span>
    </li>
  </ul>

  <div class="profile">
    <h1 class="profile__name">Lenny Firth</h1>
    <ul class="services">
      <li><svg class="tick" viewBox="0 0 10 10"><path d="M1 5l3 3 5-7" fill="none" stroke="var(--navy)" stroke-width="1.8"/></svg>Equine Performance</li>
      <li><svg class="tick" viewBox="0 0 10 10"><path d="M1 5l3 3 5-7" fill="none" stroke="var(--navy)" stroke-width="1.8"/></svg>Brindle4Ponies and Acupuncture</li>
      <li><svg class="tick" viewBox="0 0 10 10"><path d="M1 5l3 3 5-7" fill="none" stroke="var(--navy)" stroke-width="1.8"/></svg>Horsemanship Lessons and Clinics</li>
      <li><svg class="tick" viewBox="0 0 10 10"><path d="M1 5l3 3 5-7" fill="none" stroke="var(--navy)" stroke-width="1.8"/></svg>Horse Training</li>
    </ul>
  </div>

  <ul class="contact-list contact-list--online">
    <li>
      <svg class="icon" viewBox="0 0 20 20"><circle cx="10" cy="10" r="10" fill="var(--navy)"/></svg>
      <span>FB/lenny.firth.263</span>
    </li>
    <li>
      <svg class="icon" viewBox="0 0 20 20"><circle cx="10" cy="10" r="10" fill="var(--navy)"/><circle cx="10" cy="10" r="5.5" fill="none" stroke="#fff" stroke-width="1"/><path d="M4.5 10h11M10 4.5c-2.5 3-2.5 8 0 11M10 4.5c2.5 3 2.5 8 0 11" fill="none" stroke="#fff" stroke-width="1"/></svg>
      <span>www.StableArc.com.au</span>
    </li>
  </ul>
</section>

</body>
</html>
```